Tag Rugby (Sport) Website

We are looking to redesign the home page of Celtic Flag Hockey League (www.flagpuckleague.ie). We are an adult sports company, with 10,000 players around Ireland, aged 22 to 35, equally divided between male and female. Tag is a fantastic way to keep fit but to meet new people - so the website should be very clear, bright and fun to reflect the social nature of the sport.

Target Market(s)

22-35 ABC1 equally male and female.

Industry/Entity Type

Adult

Font styles to use
Sans Serif

Requirements
Must have
• It MUST have all the elements on this "home made" page. http://www.flagpuckleague.ie/defaultnew.aspx

The structure of the website has been signed off...we just require the thing to be designed and brought together

We need the 3 ad spaces to be designed:
1. Square ad on left should have following text:
Spring back into Action! Play Tag from Mar to May. Last Few Spaces Available - REGISTER NOW! (Use the Flagpuckleague.ie ball logo)

2. Top right ad to be designed with following text:
Find your Nearest Tag Venue (include icon with outline Map of Ireland)

3. Bottom right ad to be designed with following text:
Tag Events Calendar (with some calendar icon)

The dropdown menu items should be displayed vertically (not horizontally) - similar to drop downs on www.joinflagpuck.com
Nice to have
• We also require Social Media icons to be prominent (in own separate section?) on header and footer

```html
<!DOCTYPE html>
<html lang="en">
<head>
<meta charset="utf-8">
<title>Celtic Flag Hockey League – Home</title>
<link href="https://fonts.googleapis.com/css2?family=Arimo:wght@400;700&display=swap" rel="stylesheet">
<style>
:root{
  --red:#e0262b;
  --blue-link:#2a77c8;
  --orange:#f7a21b;
  --slate:#3f5164;
  --slate-line:#4d6073;
  --ink:#333;
  --muted:#777;
  --light:#f4f5f7;
  --bar:#f3f3f3;
  --white:#fff;
  --black:#111;
}
*{box-sizing:border-box;margin:0;padding:0}
html,body{width:1001px;height:1200px;overflow:hidden;background:var(--white)}
body{font-family:"Arimo",Arial,sans-serif;color:var(--ink);position:relative}
.abs{position:absolute}

/* utility bar */
.utility-bar{left:0;top:0;width:1001px;height:14px;background:var(--bar)}
.utility-links{right:281px;top:4px;font-size:6px;color:#555;white-space:nowrap;text-align:right}
.utility-social{top:2px;width:10px;height:10px;border-radius:50%;background:#555}
.utility-login{left:770px;top:4px;font-size:6px;color:#555}
.utility-login::after{content:"";display:inline-block;margin-left:6px;border:3px solid transparent;border-top:4px solid #555;vertical-align:-2px}

/* header */
.site-header{left:0;top:14px;width:1001px;height:74px;background:var(--white);box-shadow:0 1px 3px rgba(0,0,0,.08)}
.brand{left:188px;top:22px;width:68px;height:60px;display:flex;flex-direction:column;align-items:center;justify-content:center;gap:4px}
.brand-name{font-size:15px;font-weight:700;color:var(--red)}
.brand-url{font-size:5.5px;font-weight:700;color:var(--red);white-space:nowrap}
.main-nav a{position:absolute;top:67px;font-size:8px;color:#8a8a8a;text-decoration:none;white-space:nowrap}
.main-nav a.active{color:var(--blue-link)}
.nav-underline{left:439px;top:85px;width:56px;height:3px;background:var(--red)}

/* hero */
.hero{left:0;top:88px;width:1001px;height:286px;background:linear-gradient(180deg,#c9ccc6 0%,#7f9a7c 30%,#1f7a3b 60%,#145f2c 100%)}
.hero-caption{left:192px;top:276px;width:220px;height:70px;background:rgba(30,40,35,.78);padding:12px 22px;color:var(--white)}
.hero-caption::before{content:"";position:absolute;left:16px;top:0;border:7px solid transparent;border-top:7px solid var(--red)}
.hero-caption h2{font-size:14px;font-weight:400;margin-bottom:6px}
.hero-caption p{font-size:6.5px;font-weight:700;line-height:1.55}
.hero-prev{left:412px;top:318px;width:26px;height:28px;background:rgba(60,60,60,.7)}
.hero-next{left:438px;top:318px;width:28px;height:28px;background:var(--red)}
.hero-prev svg,.hero-next svg{position:absolute;left:9px;top:8px}
.hero-band{left:0;top:364px;width:1001px;height:10px;background:rgba(80,190,120,.55)}

/* feature cards */
.features{left:0;top:374px;width:1001px;height:246px;background:var(--light)}
.card{top:442px;width:139px;height:146px;background:var(--white);text-align:center}
.card-avatar{top:406px;width:74px;height:74px;border-radius:50%;background:radial-gradient(circle at 50% 40%,#c0392b 0%,#5a1d1a 55%,#151515 100%)}
.card h3{position:absolute;top:45px;left:0;width:100%;font-size:8px;font-weight:700;color:#333}
.card p{position:absolute;top:80px;left:14px;width:111px;font-size:5.5px;line-height:1.75;color:#888}
.card .btn{position:absolute;left:43px;top:138px;width:53px;height:16px;background:var(--red);color:var(--white);font-size:5.5px;font-weight:700;line-height:16px;text-align:center}

/* intro */
.intro{left:0;top:644px;width:1001px;text-align:center;font-size:11.5px;line-height:1.55;color:#555}

/* ads */
.ad-spring{left:221px;top:702px;width:267px;height:107px;background:radial-gradient(ellipse at 60% 50%,#3a3a3a 0%,#151515 80%);color:var(--white)}
.ad-spring h4{position:absolute;left:0;top:18px;width:100%;padding-left:40px;text-align:center;font-size:13px;font-weight:400}
.ball-name{left:28px;top:45px;font-size:6.5px;font-weight:700;color:var(--white);display:flex;align-items:center;gap:4px;white-space:nowrap}
.ball-name i{display:block;width:9px;height:9px;border-radius:50%;background:#3fb0d6}
.ad-spring .play{left:116px;top:44px;font-size:10px;white-space:nowrap}
.ad-spring .play b{font-weight:700}
.ad-spring .register{left:93px;top:68px;width:78px;height:22px;border-radius:5px;background:var(--white);color:var(--red);font-size:7px;font-weight:700;line-height:22px;text-align:center}

.ad-venue{left:503px;top:702px;width:258px;height:107px;background:var(--orange);overflow:hidden}
.venue-corner{left:0;top:0}
.venue-mark{left:6px;top:4px;font-size:6px;font-weight:700;color:var(--white)}
.ad-venue h4{position:absolute;left:18px;top:41px;font-size:10.5px;font-weight:400;color:var(--white);white-space:nowrap}
.venue-input{left:17px;top:56px;width:100px;height:23px;background:var(--white);font-size:6px;color:#aaa;line-height:23px;padding-left:8px}
.venue-go{left:117px;top:56px;width:31px;height:23px;background:var(--black)}
.venue-go svg{position:absolute;left:12px;top:7px}
.venue-map{left:166px;top:6px;width:84px;height:98px;border-radius:40% 30% 45% 35%;background:rgba(255,255,255,.28)}

/* news & events */
.info-band{left:0;top:847px;width:1001px;height:225px;background:var(--slate)}
.info-divider{left:467px;top:870px;width:1px;height:170px;background:var(--slate-line)}
.section-icon{width:31px;height:31px;border-radius:50%;background:var(--white)}
.section-icon svg{position:absolute;left:8px;top:8px}
.section-kicker{font-size:8px;color:var(--white);letter-spacing:.3px}
.section-title{font-size:13px;color:var(--white)}
.news-day{left:221px;top:918px;font-size:40px;font-weight:700;color:var(--white);line-height:1}
.news-month{left:221px;top:962px;font-size:17px;color:#a9b4bf;letter-spacing:.5px}
.news-head{left:277px;top:925px;width:160px;font-size:6.5px;font-weight:700;color:var(--white);line-height:1.6}
.news-body{left:277px;top:963px;width:160px;font-size:6px;color:#d6dde4;line-height:1.6}
.more-btn{top:1026px;width:47px;height:18px;background:var(--orange);color:var(--white);font-size:7px;font-weight:700;line-height:18px;text-align:center}
.event{left:529px;width:232px;height:42px;background:var(--white)}
.event-date{left:0;top:0;width:50px;height:42px;background:var(--black);color:var(--white);text-align:center;padding-top:6px;font-size:14px;line-height:1}
.event-date small{display:block;font-size:9px;margin-top:2px}
.event-thumb{left:50px;top:0;width:53px;height:42px;background:linear-gradient(135deg,#1a1a1a,#b23227 60%,#2a2a2a)}
.event-text{left:113px;top:7px;width:112px}
.event-text h5{font-size:6.5px;font-weight:700;color:#222;margin-bottom:4px}
.event-text p{font-size:5.5px;color:#555;line-height:1.5}

/* tweet strip */
.tweet-bar{left:0;top:1072px;width:1001px;height:34px;background:var(--bar)}
.tweet-dot{left:247px;top:1083px;width:12px;height:12px;border-radius:50%;background:#d5d5d5}
.tweet-divider{left:278px;top:1078px;width:1px;height:22px;background:#ddd}
.tweet-text{left:288px;top:1086px;font-size:6px;color:#333;white-space:nowrap}
.tweet-text a{color:var(--blue-link);text-decoration:none}
.tweet-text em{color:#888;margin-left:6px}
.tweet-arrows{left:667px;top:1084px}

/* footer */
.foot-social{top:1120px;width:18px;height:18px;border-radius:50%;background:#555}
.foot-links{left:0;top:1165px;width:1001px;text-align:center;font-size:5.5px;color:#555}
.foot-copy{left:0;top:1177px;width:1001px;text-align:center;font-size:5.5px;color:#777}
</style>
</head>
<body>

<div class="abs utility-bar"></div>
<div class="abs utility-links">Join | My Venue | Fixtures &amp; Results</div>
<span class="abs utility-social" style="left:727px" aria-label="Social link"></span>
<span class="abs utility-social" style="left:740px" aria-label="Social link"></span>
<span class="abs utility-social" style="left:753px" aria-label="Social link"></span>
<div class="abs utility-login">Login</div>

<header class="abs site-header"></header>
<div class="abs brand">
  <span class="brand-name">C.F.H.L.</span>
  <span class="brand-url">www.flagpuckleague.ie</span>
</div>
<nav class="main-nav">
  <a class="active" style="left:439px">Playing the Game</a>
  <a style="left:514px">Our Events</a>
  <a style="left:577px">Referees</a>
  <a style="left:632px">News</a>
  <a style="left:678px">Gallery</a>
  <a style="left:727px">About Us</a>
  <a style="left:781px">Shop</a>
</nav>
<div class="abs nav-underline"></div>

<section class="abs hero" role="img" aria-label="Photo of a mixed team of players in green jerseys lined up arm in arm"></section>
<div class="abs hero-band"></div>
<div class="abs hero-caption">
  <h2>Lorem ipsum dolor sit</h2>
  <p>Lorem ipsum dolor sit amet, consectetur adipisicing elit, sed do eiusmod tempor incididunt ut labore et dolore magna aliqua.</p>
</div>
<div class="abs hero-prev"><svg width="8" height="12"><path d="M7 1 L2 6 L7 11" stroke="#bbb" stroke-width="1.4" fill="none"/></svg></div>
<div class="abs hero-next"><svg width="8" height="12"><path d="M1 1 L6 6 L1 11" stroke="#fff" stroke-width="1.4" fill="none"/></svg></div>

<section class="abs features"></section>
<article class="abs card" style="left:192px"><h3>Lorem ipsum dolor sit amet</h3><p>Lorem ipsum dolor sit amet, consectetur adipiscing elit, sed dia nonummy nibh euismod tincidut. laoreet dolore magna aliquam erat ventrim.</p><span class="btn">READ MORE</span></article>
<article class="abs card" style="left:347px"><h3>Lorem ipsum dolor sit amet</h3><p>Lorem ipsum dolor sit amet, consectetur adipiscing elit, sed dia nonummy nibh euismod tincidut. laoreet dolore magna aliquam erat ventrim.</p><span class="btn">READ MORE</span></article>
<article class="abs card" style="left:502px"><h3>Lorem ipsum dolor sit amet</h3><p>Lorem ipsum dolor sit amet, consectetur adipiscing elit, sed dia nonummy nibh euismod tincidut. laoreet dolore magna aliquam erat ventrim.</p><span class="btn">READ MORE</span></article>
<article class="abs card" style="left:656px"><h3>Lorem ipsum dolor sit amet</h3><p>Lorem ipsum dolor sit amet, consectetur adipiscing elit, sed dia nonummy nibh euismod tincidut. laoreet dolore magna aliquam erat ventrim.</p><span class="btn">READ MORE</span></article>
<div class="abs card-avatar" style="left:224px" role="img" aria-label="Player photo"></div>
<div class="abs card-avatar" style="left:379px" role="img" aria-label="Player photo"></div>
<div class="abs card-avatar" style="left:534px" role="img" aria-label="Player photo"></div>
<div class="abs card-avatar" style="left:688px" role="img" aria-label="Player photo"></div>

<p class="abs intro">Lorem ipsum dolor sit amet, consectetur adipisicing elit, sed do eiusmod tempor<br>incididunt ut labore et dolore magna aliqua.</p>

<aside class="abs ad-spring" role="img" aria-label="Dark action photo background for the spring season ad">
  <h4>Spring back into Action!</h4>
  <div class="abs ball-name"><i></i>Flagpuckleague.ie</div>
  <div class="abs play">Play Tag from <b>Mar to May</b></div>
  <div class="abs register">REGISTER NOW!</div>
</aside>

<aside class="abs ad-venue">
  <svg class="abs venue-corner" width="80" height="48"><polygon points="0,0 80,0 0,48" fill="#111"/></svg>
  <span class="abs venue-mark">C.F.H.L.</span>
  <div class="abs venue-map" role="img" aria-label="Outline map of Ireland"></div>
  <h4>Find your Nearest Tag Venue</h4>
  <div class="abs venue-input">Enter Zip Code</div>
  <div class="abs venue-go"><svg width="8" height="10"><polygon points="0,0 8,5 0,10" fill="#fff"/></svg></div>
</aside>

<section class="abs info-band"></section>
<div class="abs info-divider"></div>

<div class="abs section-icon" style="left:222px;top:874px"><svg width="15" height="15"><rect x="1" y="2" width="13" height="11" fill="none" stroke="#3f5164" stroke-width="1.3"/><line x1="4" y1="6" x2="11" y2="6" stroke="#3f5164"/><line x1="4" y1="9" x2="11" y2="9" stroke="#3f5164"/></svg></div>
<div class="abs section-kicker" style="left:265px;top:879px">LATEST</div>
<div class="abs section-title" style="left:265px;top:889px">NEWS</div>
<div class="abs news-day">21</div>
<div class="abs news-month">JULY</div>
<div class="abs news-head">LOREM IPSUM DOLOR SIT AMET, CONSECTETUR ADIPISICING ELIT</div>
<div class="abs news-body">Ut enim ad minim veniam, quis nostrud exercitation ullamco laboris nisi ut aliquip ex ea commodo conse-quat. Duis aute irure</div>
<div class="abs more-btn" style="left:280px">more &nbsp;→</div>

<div class="abs section-icon" style="left:529px;top:874px"><svg width="15" height="15"><rect x="1" y="3" width="13" height="11" fill="none" stroke="#3f5164" stroke-width="1.3"/><line x1="1" y1="6" x2="14" y2="6" stroke="#3f5164"/><line x1="4" y1="1" x2="4" y2="4" stroke="#3f5164"/><line x1="11" y1="1" x2="11" y2="4" stroke="#3f5164"/></svg></div>
<div class="abs section-kicker" style="left:567px;top:879px">UPCOMING</div>
<div class="abs section-title" style="left:567px;top:889px">EVENTS</div>

<div class="abs event" style="top:924px">
  <div class="abs event-date">12<small>Oct</small></div>
  <div class="abs event-thumb" role="img" aria-label="Event photo"></div>
  <div class="abs event-text"><h5>Lorem Ipsum</h5><p>Lorem ipsum dolor sit amet, consectetur adipiscing elit, sed do eiusmod tempor</p></div>
</div>
<div class="abs event" style="top:972px">
  <div class="abs event-date">12<small>Oct</small></div>
  <div class="abs event-thumb" role="img" aria-label="Event photo"></div>
  <div class="abs event-text"><h5>Lorem Ipsum</h5><p>Lorem ipsum dolor sit amet, consectetur adipiscing elit, sed do eiusmod tempor</p></div>
</div>
<div class="abs more-btn" style="left:529px">more &nbsp;→</div>

<div class="abs tweet-bar"></div>
<div class="abs tweet-dot"></div>
<div class="abs tweet-divider"></div>
<p class="abs tweet-text"><a>http://example.com/abc/</a> Lorem ipsum dolor sit amet, consectetur adipisicing elit, sed do eiusmod tempor incididunt <em>- 2min ago</em></p>
<svg class="abs tweet-arrows" width="24" height="10"><path d="M5 1 L1 5 L5 9" stroke="#bbb" fill="none"/><path d="M17 1 L21 5 L17 9" stroke="#bbb" fill="none"/></svg>

<span class="abs foot-social" style="left:463px" aria-label="Social link"></span>
<span class="abs foot-social" style="left:486px" aria-label="Social link"></span>
<span class="abs foot-social" style="left:509px" aria-label="Social link"></span>
<div class="abs foot-links">Login &nbsp;|&nbsp; Change your Country &nbsp;|&nbsp; Terms of Use &nbsp;|&nbsp; Privacy Policy &nbsp;|&nbsp; Terms &amp; Conditions</div>
<div class="abs foot-copy">Copyright© 2014 CFHL. All rights reserved.</div>

</body>
</html>
```